Business card revamp

we are refrigeration mechanic i need a modern professional double side business card using my current branding
The card information must have site address~ 17 Whitlow st Tallira, Vic 3713 postal address~ P.o. Box 862 Tallira,Vic 3712 Phone Number~0358149637 Fax Nunber~0358260518 Email address~ brucet@pelvanor.com.au Title~ Manager Licence numbers~ AU47391, NSW 681329K Web site~ www.frostrimvane.com.au

Industry/Entity Type

Business

```html
<!DOCTYPE html>
<html lang="en">
<head>
<meta charset="utf-8">
<title>FrostRimVane business card</title>
<link rel="stylesheet" href="https://fonts.googleapis.com/css2?family=Mulish:wght@400;600;700;800&display=swap">
<style>
  :root {
    --page-bg: #e9e9e9;
    --card-dark-1: #2a2a2b;
    --card-dark-2: #3b3b3c;
    --card-light: #ffffff;
    --brand-red: #b3262b;
    --brand-blue: #1d5fa8;
    --text-grey: #8a8a8a;
    --text-light: #e6e6e6;
  }
  * { margin: 0; padding: 0; box-sizing: border-box; }
  html, body { width: 1200px; height: 720px; overflow: hidden; }
  body {
    background: var(--page-bg);
    font-family: "Mulish", sans-serif;
    position: relative;
  }
  .card {
    position: absolute;
    top: 241px;
    width: 420px;
    height: 240px;
    box-shadow: 0 6px 16px rgba(0,0,0,0.2);
  }
  .card--front {
    left: 147px;
    background: linear-gradient(160deg, var(--card-dark-2), var(--card-dark-1));
  }
  .card--back {
    left: 633px;
    background: var(--card-light);
  }
  .front-brand {
    position: absolute;
    left: 0; right: 0; top: 92px;
    text-align: center;
    color: var(--brand-red);
    font-weight: 800;
    font-size: 36px;
    line-height: 42px;
    letter-spacing: 3px;
    text-transform: uppercase;
  }
  .front-tagline {
    position: absolute;
    left: 0; right: 0; top: 129px;
    text-align: center;
    color: var(--text-light);
    font-size: 10.5px;
    letter-spacing: 1.8px;
    text-transform: uppercase;
  }
  .front-web {
    position: absolute;
    left: 0; right: 0; top: 207px;
    text-align: center;
    color: var(--text-light);
    font-size: 13px;
  }
  .back-brand {
    position: absolute;
    left: 13px; top: 36px;
    color: var(--brand-red);
    font-weight: 800;
    font-size: 21px;
    line-height: 26px;
    letter-spacing: 1.4px;
    text-transform: uppercase;
  }
  .back-tagline {
    position: absolute;
    left: 41px; top: 58px;
    color: var(--text-grey);
    font-size: 6px;
    letter-spacing: 0.8px;
    text-transform: uppercase;
  }
  .licence {
    position: absolute;
    left: 14px; top: 89px;
    color: var(--text-grey);
    font-weight: 700;
    font-size: 11px;
    line-height: 14.5px;
  }
  .person {
    position: absolute;
    right: 15px; top: 104px;
    text-align: right;
  }
  .person-name { color: var(--brand-red); font-weight: 700; font-size: 16px; line-height: 21px; }
  .person-title { color: var(--brand-blue); font-size: 12.5px; line-height: 17px; }
  .contact {
    position: absolute;
    left: 15px;
    font-size: 11px;
    line-height: 14px;
    color: var(--brand-blue);
  }
  .contact .label { color: var(--brand-red); font-weight: 700; }
  .contact--phone { top: 128px; }
  .contact--email { top: 165px; }
  .contact--address { top: 190px; line-height: 16px; }
</style>
</head>
<body>
  <section class="card card--front">
    <div class="front-brand">FrostRimVane</div>
    <div class="front-tagline">Heating and cooling specialists</div>
    <div class="front-web">frostrimvane.com.au</div>
  </section>

  <section class="card card--back">
    <div class="back-brand">FrostRimVane</div>
    <div class="back-tagline">Heating and cooling specialists</div>

    <div class="licence">Licence # AU47391<br>NSW 681329K</div>

    <div class="person">
      <div class="person-name">Bruce Talvanek</div>
      <div class="person-title">Manager</div>
    </div>

    <div class="contact contact--phone">
      <span class="label">Ph:</span> 035.814.9637<br>
      <span class="label">Fax:</span> 03.582.60518
    </div>
    <div class="contact contact--email">
      <span class="label">Email:</span> brucet@pelvanor.com.au
    </div>
    <div class="contact contact--address">
      <span class="label">Postal Address:</span> P.O. Box 862 Tallira,Vic 3712<br>
      <span class="label">Site Address:</span> 17 Whitlow st Tallira, Vic 3713
    </div>
  </section>
</body>
</html>
```